Poster for a vegan café with a funny message about the food served.

Design a poster with the text "Eating here was a big missed stake!" for a café at a meditation center (lunavardet.se).

```html
<!DOCTYPE html>
<html lang="en">
<head>
<meta charset="UTF-8">
<title>Missed Stake Poster</title>
<link href="https://fonts.googleapis.com/css2?family=Montserrat:wght@800&display=swap" rel="stylesheet">
<style>
  :root {
    --backdrop: #3d3b3a;
    --paper: #c9c1bf;
    --ring-yellow: #efde4c;
    --block-red: #d1232b;
    --block-green: #1f8c5e;
    --block-blue: #2c5aa3;
    --block-gold: #c6a12c;
    --headline: #ffffff;
    --photo-light: #d8d2d0;
    --photo-dark: #8e8684;
  }
  html, body {
    margin: 0;
    padding: 0;
    width: 1200px;
    height: 1198px;
    overflow: hidden;
    background: var(--backdrop);
  }
  .poster {
    position: absolute;
    left: 207px;
    top: 75px;
    width: 788px;
    height: 1050px;
    background: var(--paper);
    overflow: hidden;
  }
  .rings {
    position: absolute;
    left: 0;
    top: 0;
  }
  .portrait {
    position: absolute;
    left: 0;
    top: 45px;
    width: 560px;
    height: 1005px;
    border-radius: 240px 240px 0 0;
    background: radial-gradient(ellipse at 48% 30%, var(--photo-light) 0%, #b3abaa 45%, var(--photo-dark) 100%);
  }
  .block {
    position: absolute;
    mix-blend-mode: multiply;
  }
  .block-red   { left: 93px;  top: 596px; width: 283px; height: 159px; background: var(--block-red); }
  .block-green { left: 353px; top: 620px; width: 332px; height: 148px; background: var(--block-green); }
  .block-blue  { left: 0;     top: 730px; width: 423px; height: 188px; background: var(--block-blue); }
  .block-gold  { left: 376px; top: 768px; width: 412px; height: 169px; background: var(--block-gold); }
  .headline {
    position: absolute;
    left: 110px;
    top: 624px;
    margin: 0;
    font-family: 'Montserrat', sans-serif;
    font-weight: 800;
    font-size: 84px;
    line-height: 94px;
    letter-spacing: -2px;
    color: var(--headline);
    white-space: nowrap;
  }
</style>
</head>
<body>
  <main class="poster">
    <svg class="rings" width="788" height="1050" viewBox="0 0 788 1050" aria-hidden="true">
      <g fill="none" stroke="var(--ring-yellow)" stroke-width="13">
        <circle cx="505" cy="190" r="180"/>
        <circle cx="470" cy="195" r="145"/>
        <circle cx="450" cy="200" r="102"/>
      </g>
    </svg>
    <div class="portrait" role="img" aria-label="Black and white photo of a surprised young woman in a denim shirt, holding her round glasses with both hands"></div>
    <div class="block block-red"></div>
    <div class="block block-green"></div>
    <div class="block block-blue"></div>
    <div class="block block-gold"></div>
    <h1 class="headline">“Eating here<br>was a big<br>missed stake!”</h1>
  </main>
</body>
</html>
```